'Fuel in Crate' flyer design.

We need a flyer design for a new company called 'Fuel in crate'. We deliver high protein, frozen meals to people in their homes. Mainly aiming at the fitness community. The flyer size will be DL (210mm x 99mm).

We already have a logo as attached below, and would obviously like it to be on the flyer somewhere. We would also like the overall design of the flyer to be in line with the logo (so that the design of the flyer works with the logo and does not contrast it too much).

If you are using any visuals (pictures, background pictures etc.) please do not reference it to any food. Rather we prefer if you used fitness as your inspiration. Please see the picture of Gustav attached for guide. If you are stuck for ideas you can use this photo, however drawn in art. Any pictures you do use please ensure that you have copyright privileges to.

Be as creative as you like with the flyer design. The logo has limited colors however we do not want the flyer to look boring!

These texts will be included on the flyer in the exact order as follows:

- Live a busy lifestyle? No time to meal prep? We do it for you!

- Whether you're bodybuilding or just want truly healthy meals, order from us online.

- Grab and Go meals that you can take to work, school...anywhere.

- High protein, low fat, low sodium.

- No artificial flavours, colours or preservatives.

- Delivered straight to your door, on the day of your choice^.

- Affordable prices.

Remember, if you fail to plan then you plan to fail.

Visit us at www.fuelincrate.com.au

^Please visit website for conditions.

Target Market(s)

Fitness community.

Industry/Entity Type

Fitness

Requirements
Must have
• Overall design must work with logo.
Nice to have
• Colors.
Should not have
• Any pictures in reference to food.

```html
<!DOCTYPE html>
<html lang="en">
<head>
<meta charset="utf-8">
<title>Fuel in Crate – DL Flyer</title>
<link rel="stylesheet" href="https://fonts.googleapis.com/css2?family=Russo+One&family=Oswald:wght@400;500;600&family=Roboto+Condensed:wght@700&display=swap">
<style>
  :root {
    --red: #c8102e;
    --red-dark: #8e0b1f;
    --black: #111111;
    --ink: #222222;
    --grey-light: #e6e6e6;
    --grey-mid: #bdbdbd;
    --white: #ffffff;
    --stage: #3a3a3a;
  }
  * { margin: 0; padding: 0; box-sizing: border-box; }
  html, body { width: 1200px; height: 2162px; overflow: hidden; background: var(--stage); }
  .flyer {
    position: absolute; left: 90px; top: 33px;
    width: 1020px; height: 2096px;
    background: var(--white); overflow: hidden;
  }
  .shapes { position: absolute; inset: 0; }
  .abs { position: absolute; }
  .headline { left: 56px; font-family: "Russo One", sans-serif; line-height: 1.02; color: var(--black); text-transform: uppercase; }
  .headline--busy { top: 58px; font-size: 58px; }
  .headline--prep { top: 210px; font-size: 51px; }
  .headline--us { top: 342px; font-size: 54px; color: var(--red); }
  .brand {
    left: 560px; top: 800px; width: 410px;
    display: flex; align-items: center; gap: 16px;
    font-family: "Russo One", sans-serif; font-size: 44px; color: var(--red);
    text-transform: uppercase; white-space: nowrap;
  }
  .brand__mark { width: 34px; height: 34px; background: var(--black); flex: none; }
  .intro {
    left: 0; width: 1020px; top: 948px; text-align: center;
    font-family: "Russo One", sans-serif; font-size: 45px; line-height: 1.1;
    color: var(--red); text-transform: uppercase;
  }
  .cta {
    left: 263px; top: 1068px; width: 498px; height: 148px; text-align: center;
    font-family: "Oswald", sans-serif; color: var(--white); text-transform: uppercase;
  }
  .cta__small { display: block; font-size: 40px; line-height: 1; padding-top: 14px; font-weight: 400; }
  .cta__big { display: block; font-size: 82px; line-height: 1; font-weight: 500; }
  .grab {
    left: 0; width: 1020px; top: 1290px; text-align: center;
    font-family: "Oswald", sans-serif; text-transform: uppercase; color: var(--ink); font-weight: 500;
  }
  .grab__line1 { font-size: 92px; line-height: 1.05; }
  .grab__line2 { font-size: 80px; line-height: 1.12; }
  .grab__line3 { font-size: 74px; line-height: 1.12; color: var(--red); }
  .benefits {
    left: 0; width: 1020px; top: 1556px; list-style: none;
    font-family: "Oswald", sans-serif; font-size: 30px; text-transform: uppercase;
  }
  .benefit {
    display: flex; justify-content: center; align-items: center; gap: 18px;
    height: 57px;
  }
  .benefit--red { color: var(--red); }
  .benefit--dark { color: var(--black); }
  .chev { width: 44px; height: 22px; flex: none; }
  .motto {
    left: 50px; top: 1980px;
    font-family: "Roboto Condensed", sans-serif; font-weight: 700; font-size: 35px; line-height: 1.2; color: var(--white);
  }
  .visit {
    right: 40px; top: 1905px; text-align: right; color: var(--white);
    font-family: "Roboto Condensed", sans-serif; font-weight: 700;
  }
  .visit__label { font-size: 36px; line-height: 1.1; }
  .visit__url { font-size: 42px; line-height: 1.2; }
  .visit__note { font-family: "Oswald", sans-serif; font-weight: 400; font-size: 20px; line-height: 1.35; margin-top: 14px; }
</style>
</head>
<body>
<main class="flyer">
  <svg class="shapes" width="1020" height="2096" viewBox="0 0 1020 2096" aria-hidden="true">
    <defs>
      <linearGradient id="panelGrey" x1="0" y1="0" x2="1" y2="1">
        <stop offset="0" stop-color="#f2f2f2"/>
        <stop offset="1" stop-color="#cfcfcf"/>
      </linearGradient>
      <linearGradient id="ribbonRed" x1="0" y1="0" x2="1" y2="0">
        <stop offset="0" stop-color="#8e0b1f"/>
        <stop offset="1" stop-color="#d41535"/>
      </linearGradient>
      <linearGradient id="photoTone" x1="0" y1="0" x2="1" y2="1">
        <stop offset="0" stop-color="#9a8576"/>
        <stop offset="0.5" stop-color="#4a3c34"/>
        <stop offset="1" stop-color="#1e1a18"/>
      </linearGradient>
    </defs>
    <!-- top panel -->
    <polygon points="0,0 1020,0 1020,1000 0,880" fill="url(#panelGrey)"/>
    <!-- black wedge -->
    <polygon points="0,610 470,800 0,900" fill="var(--black)"/>
    <!-- red wedge -->
    <polygon points="180,500 560,800 90,730" fill="var(--red)"/>
    <!-- white lower area -->
    <polygon points="0,900 470,800 1020,1010 1020,2096 0,2096" fill="var(--white)"/>
  </svg>

  <svg class="abs" style="left:0;top:0" width="1020" height="800" viewBox="0 0 1020 800" role="img" aria-label="Photo of a muscular athlete doing a dumbbell curl in a gym">
    <polygon points="330,0 1020,0 1020,700 640,740 300,470" fill="url(#photoTone)"/>
    <polygon points="950,270 1020,200 1020,400" fill="var(--red)"/>
  </svg>

  <svg class="shapes" width="1020" height="2096" viewBox="0 0 1020 2096" aria-hidden="true">
    <!-- order banner -->
    <polygon points="290,1068 740,1068 790,1142 740,1216 290,1216 240,1142" fill="var(--red)"/>
    <!-- bottom ribbon and band -->
    <polygon points="1020,1700 1020,1870 820,1900 0,1960 0,1880 700,1820" fill="url(#ribbonRed)"/>
    <polygon points="1020,1860 1020,2096 0,2096 0,1955 820,1890" fill="var(--black)"/>
  </svg>

  <h1 class="abs headline headline--busy">Live a busy<br>lifestyle?</h1>
  <p class="abs headline headline--prep">No time to<br>meal prep?</p>
  <p class="abs headline headline--us">We do it<br>for you!</p>

  <div class="abs brand"><span class="brand__mark"></span>Fuel in Crate</div>

  <p class="abs intro">Whether you're bodybuilding or<br>just want truly healthy meals</p>

  <p class="abs cta"><span class="cta__small">Order from us</span><span class="cta__big">Online</span></p>

  <p class="abs grab">
    <span class="grab__line1">Grab and go meals</span><br>
    <span class="grab__line2">that you can take to</span><br>
    <span class="grab__line3">Work, school...anywhere</span>
  </p>

  <ul class="abs benefits">
    <li class="benefit benefit--red">
      <svg class="chev" viewBox="0 0 44 22"><polygon points="44,0 12,0 0,11 12,22 44,22 32,11" fill="var(--red)"/></svg>
      High protein, low fat**, low sodium
      <svg class="chev" viewBox="0 0 44 22"><polygon points="0,0 32,0 44,11 32,22 0,22 12,11" fill="var(--red)"/></svg>
    </li>
    <li class="benefit benefit--dark">
      <svg class="chev" viewBox="0 0 44 22"><polygon points="44,0 12,0 0,11 12,22 44,22 32,11" fill="var(--black)"/></svg>
      No artificial flavours, colours or preservatives
      <svg class="chev" viewBox="0 0 44 22"><polygon points="0,0 32,0 44,11 32,22 0,22 12,11" fill="var(--black)"/></svg>
    </li>
    <li class="benefit benefit--red">
      <svg class="chev" viewBox="0 0 44 22"><polygon points="44,0 12,0 0,11 12,22 44,22 32,11" fill="var(--red)"/></svg>
      Delivered straight to your door, on the day of your choice*
      <svg class="chev" viewBox="0 0 44 22"><polygon points="0,0 32,0 44,11 32,22 0,22 12,11" fill="var(--red)"/></svg>
    </li>
    <li class="benefit benefit--dark">
      <svg class="chev" viewBox="0 0 44 22"><polygon points="44,0 12,0 0,11 12,22 44,22 32,11" fill="var(--black)"/></svg>
      Affordable prices
      <svg class="chev" viewBox="0 0 44 22"><polygon points="0,0 32,0 44,11 32,22 0,22 12,11" fill="var(--black)"/></svg>
    </li>
  </ul>

  <p class="abs motto">Remember, if you fail to plan<br>then you plan to fail</p>

  <div class="abs visit">
    <p class="visit__label">Visit us at</p>
    <p class="visit__url">www.fuelincrate.com.au</p>
    <p class="visit__note">*Please visit us online for conditions.<br>**Our meals are low in saturated fats.</p>
  </div>
</main>
</body>
</html>
```